SINGLE PAGE WEBSITE needed for Haunted-House Style Horror Event!

PROJECT:
Single page website to advertise "Bolting Shadows"

ABOUT BOLTING SHADOWS:
Bolting Shadows is a Horror Experience event, that will be held on June 1st 2019 at The Ember Playhouse in Sydney.

At the event, patrons will enter 6 different rooms and have a horror experience in each one.

There's a bar on-site for them to drink as well.

NEEDS FOR THE WEBSITE:
1. Video banner at top, and scrolling photos after video finishes, and text over the top of the video with the name and date of the event
eg.
"A Night of Immersive Horror Experiences"
"The Ember Playhouse | June 1st, 2019"

2. Multiple Book Now buttons on the page, which will link to an external booking platform

3. It should say somewhere "Produced by [MARBLE LANTERN PRODUCTIONS LOGO]"

4. A "Next Steps" section that has the steps for them to complete, such as
- Purchase your ticket HERE for one of our waves
- Rock up at the Ember Playhouse on June 1st at your wave time
- Experience each of our 6 Interactive Horror Rooms
- Grab some drinks at the bar, a bite to eat, and enjoy a fantastic night out!

Other things that should be included somewhere:
- Testimonials
- FAQs (maybe as a dropdown, so it doesn't take up much space?)
- Contact Form on Footer

- - - -

Images, logos, and more attached!

Industry/Entity Type

Events

Coding

Coded - Design and coding required

Number of Pages Required

1 page

Requirements
Nice to have
• 1. Video banner at top, and scrolling photos after video finishes, and text over the top of the video with the name and date of the event
• eg.
• "A Night of Immersive Horror Experiences"
• "The Ember Playhouse | June 1st, 2019"
• 2. multiple Book Now buttons on the page, which will link to an external booking platform
• 3. It should say somewhere "Produced by [Marble Lantern Productions LOGO]" with the Marble Lantern logo
• 4. A "Next Steps" section that has the steps for them to complete, such as
• - Purchase your ticket HERE for one of our waves
• - Rock up at the Ember Playhouse on June 1st at your wave time
• - Experience each of our 6 Interactive Horror Rooms
• - Grab some drinks at the bar, a bite to eat, and enjoy a fantastic night out!
• Other things that should be included somewhere:
• - Testimonials
• - FAQs (maybe as a dropdown, so it doesn't take up much space?)
• - Contact Form on Footer

```html
<!DOCTYPE html>
<html lang="en">
<head>
<meta charset="utf-8">
<title>Bolting Shadows – A Night of Immersive Horror Experiences</title>
<link href="https://fonts.googleapis.com/css2?family=Oswald:wght@400;600;700&family=Lato:wght@400;700&display=swap" rel="stylesheet">
<style>
:root{
  --green:#9bd31f;
  --green-dark:#5f8a10;
  --black:#080808;
  --panel:#141414;
  --line:#2a2a2a;
  --white:#ffffff;
  --grey:#b8b8b8;
  --field:#1c1c1c;
}
*{box-sizing:border-box;margin:0;padding:0}
html,body{width:1200px;height:3748px;overflow:hidden}
body{
  position:relative;
  background:
    radial-gradient(ellipse 500px 700px at 120px 2750px,#1f221c 0%,transparent 70%),
    radial-gradient(ellipse 450px 600px at 1080px 3300px,#1d1f1b 0%,transparent 70%),
    radial-gradient(ellipse 500px 500px at 1050px 1400px,#1a1a1a 0%,transparent 70%),
    var(--black);
  color:var(--white);
  font-family:"Lato",Arial,sans-serif;
}
.abs{position:absolute}
.heading{font-family:"Oswald",Impact,sans-serif;font-weight:700;font-style:italic;text-transform:uppercase;letter-spacing:1px}

/* decoration */
.splat{position:absolute;background:var(--green);border-radius:50%;filter:blur(1px)}
.figure-fill{position:absolute;border-radius:40% 40% 20% 20%}

/* nav */
.site-header{left:0;top:0;width:1200px;height:120px}
.brand{left:240px;top:28px;font-family:"Oswald",Impact,sans-serif;font-weight:700;font-size:38px;color:var(--green);letter-spacing:1px;display:flex;align-items:center;gap:12px}
.brand .mark{width:22px;height:22px;background:var(--green)}
.nav{left:660px;top:50px;display:flex;gap:34px;font-family:"Oswald",sans-serif;font-size:15px;font-weight:600;text-transform:uppercase}
.nav a{color:var(--white);text-decoration:none}
.nav a.active{color:var(--green)}

/* hero */
.hero-side{top:225px;width:220px;text-align:center}
.hero-side.left{left:10px}
.hero-side.right{left:985px;width:205px}
.hero-side .big{font-size:31px;line-height:36px;color:var(--white);letter-spacing:0}
.hero-side .big span{color:var(--green)}
.hero-side .venue{font-size:20px;line-height:26px;color:var(--green);margin-top:10px;letter-spacing:0}
.hero-video{left:240px;top:140px;width:740px;height:440px;border:8px solid var(--green);
  background:radial-gradient(ellipse at center,#2c3a14 0%,#10150a 60%,#050505 100%)}
.play{position:absolute;left:332px;top:40px;width:60px;height:60px;border-radius:50%;background:rgba(255,255,255,.85)}
.play::after{content:"";position:absolute;left:24px;top:18px;border-left:18px solid #111;border-top:12px solid transparent;border-bottom:12px solid transparent}
.hero-video .brand-lg{position:absolute;left:0;right:0;top:110px;text-align:center;font-family:"Oswald",Impact,sans-serif;font-weight:700;font-size:66px;line-height:90px;color:var(--green);letter-spacing:2px}
.hero-video .tag{position:absolute;left:0;right:0;top:235px;text-align:center;font-size:26px;color:var(--white)}
.hero-video .info{position:absolute;left:0;right:0;top:290px;text-align:center;font-size:16px;line-height:26px;color:var(--grey)}

/* gallery */
.gallery{left:260px;top:600px;width:680px;display:grid;grid-template-columns:repeat(3,1fr);gap:20px}
.photo{height:170px;background:linear-gradient(135deg,#3a2a2a,#141414)}
.photo.green{outline:4px solid var(--green)}

/* section heading */
.sec-title{left:0;width:1200px;text-align:center}
.sec-title .kicker{display:inline-block;background:var(--green);color:#000;padding:0 12px;font-size:22px;line-height:30px}
.sec-title h2{font-size:34px;line-height:40px}

/* feature boxes */
.features{left:220px;top:1300px;width:760px;display:flex;gap:24px}
.feature{flex:1;text-align:center}
.feature .box{height:110px;border:3px solid var(--green);display:flex;align-items:center;justify-content:center;font-family:"Oswald",sans-serif;font-size:13px;font-weight:600}
.btn{display:inline-block;background:var(--green);color:#000;font-family:"Oswald",sans-serif;font-weight:700;font-size:11px;text-transform:uppercase;padding:4px 14px;margin-top:14px}
.dots{left:580px;top:1484px;display:flex;gap:8px}
.dots i{width:8px;height:8px;border-radius:50%;background:#666}
.dots i:first-child{background:var(--white)}

/* produced by */
.produced{left:200px;top:1560px;width:800px;height:170px}
.produced .photo-band{position:absolute;left:0;top:0;width:330px;height:170px;background:linear-gradient(120deg,#5a1a1a,#2d2d2d 60%,#cfcfcf);clip-path:polygon(0 8%,100% 0,88% 100%,0 92%)}
.produced .green-band{position:absolute;left:250px;top:0;width:550px;height:170px;background:var(--green);clip-path:polygon(12% 0,100% 6%,98% 94%,0 100%)}
.produced .label{position:absolute;left:340px;top:48px;width:210px;font-size:36px;line-height:40px;color:#000;text-align:center}
.produced .partner{position:absolute;left:580px;top:55px;width:190px;height:62px;background:#111;display:flex;align-items:center;justify-content:center;text-align:center;font-family:"Oswald",sans-serif;font-weight:600;font-size:14px;line-height:17px;color:var(--white)}

/* steps */
.steps{left:200px;top:1960px;width:800px;display:flex;gap:24px}
.step{flex:1;text-align:center;font-size:21px;line-height:26px}
.step span{color:var(--green)}

/* testimonials */
.sec-title.plain h2{display:inline-block;border-bottom:3px solid var(--green);padding:0 6px}
.testimonials{left:240px;top:2215px;width:720px;display:flex;gap:24px}
.quote{flex:1}
.quote .card{position:relative;height:100px;padding:12px;font-size:11px;line-height:15px;background:var(--white);color:#333}
.quote.featured .card{background:var(--green);color:#000}
.quote .card::after{content:"";position:absolute;left:22px;bottom:-12px;border-top:12px solid var(--white);border-right:12px solid transparent}
.quote.featured .card::after{border-top-color:var(--green)}
.quote .who{display:flex;align-items:center;gap:12px;margin-top:30px;font-family:"Oswald",sans-serif;font-size:14px;font-weight:600}
.quote .avatar{width:40px;height:40px;border-radius:50%;background:linear-gradient(#6b5a4e,#2b2220);border:2px solid var(--white)}

/* faq */
.faq{left:220px;top:2545px;width:760px}
.faq-item{display:flex;justify-content:space-between;align-items:center;height:46px;padding:0 16px;border-bottom:1px solid var(--line);font-size:14px;font-style:italic}
.faq-item b{color:var(--green);font-style:normal;font-size:20px}
.faq-item.open{background:var(--green);color:#000;border:none}
.faq-item.open b{color:#000}
.faq-answer{padding:14px 16px;font-size:12px;line-height:18px;color:var(--grey)}

/* booking */
.book-title h2{display:inline-block;border-bottom:3px solid var(--green);padding:0 10px}
.call{left:280px;top:3030px;width:640px;text-align:center;font-size:20px;line-height:28px;color:var(--green)}
.form{left:280px;top:3100px;width:640px;display:grid;grid-template-columns:1fr 1fr;gap:14px 20px}
.field{height:40px;background:var(--field);border:1px solid var(--line);color:#888;font-size:12px;padding:12px}
.field.wide{grid-column:1 / 3;height:150px}
.submit{left:570px;top:3466px}

/* footer */
.footer-brand{left:0;top:3580px;width:1200px;text-align:center;font-family:"Oswald",Impact,sans-serif;font-weight:700;font-size:54px;color:var(--green);letter-spacing:2px}
.copy{left:0;top:3680px;width:1200px;text-align:center;font-size:11px;color:#888}
</style>
</head>
<body>

<!-- decorative fills -->
<div class="figure-fill" role="img" aria-label="Green running figure silhouette" style="left:20px;top:1190px;width:150px;height:280px;background:var(--green);opacity:.9"></div>
<div class="figure-fill" role="img" aria-label="Green running figure silhouette" style="left:1060px;top:3020px;width:130px;height:300px;background:var(--green);opacity:.9"></div>
<div class="figure-fill" role="img" aria-label="Faded horror character in the darkness" style="left:40px;top:2200px;width:300px;height:700px;background:linear-gradient(#2a2c28,transparent);opacity:.7"></div>
<div class="figure-fill" role="img" aria-label="Faded horror character in the darkness" style="left:900px;top:1180px;width:280px;height:400px;background:linear-gradient(#242424,transparent);opacity:.7"></div>
<div class="splat" role="img" aria-label="Green paint splatter" style="left:0;top:140px;width:60px;height:90px;opacity:.6"></div>
<div class="splat" role="img" aria-label="Green paint splatter" style="left:1140px;top:140px;width:60px;height:90px;opacity:.6"></div>
<div class="splat" role="img" aria-label="Green paint splatter" style="left:1150px;top:1380px;width:50px;height:60px"></div>
<div class="splat" role="img" aria-label="White paint splatter" style="left:1130px;top:2500px;width:70px;height:90px;background:#fff"></div>
<div class="splat" role="img" aria-label="Green paint splatter" style="left:0;top:3250px;width:50px;height:60px"></div>

<header class="site-header abs">
  <div class="brand abs"><span class="mark"></span>BOLTING SHADOWS</div>
  <nav class="nav abs">
    <a class="active" href="#about">About</a>
    <a href="#testimonials">Testimonials</a>
    <a href="#faq">FAQ</a>
    <a href="#contact">Contact</a>
  </nav>
</header>

<div class="hero-side left abs heading">
  <div class="big">A Night <br>of <span>Immersive</span><br><span>Horror</span><br>Experiences</div>
  <div class="venue">The Ember Playhouse<br>| June 1st, 2019</div>
</div>
<div class="hero-side right abs heading">
  <div class="big">A Night <br>of <span>Immersive</span><br><span>Horror</span><br>Experiences</div>
  <div class="venue">The Ember Playhouse<br>| June 1st, 2019</div>
</div>

<section class="hero-video abs" role="img" aria-label="Event video banner with dark green smoky horror scene">
  <div class="play"></div>
  <div class="brand-lg">BOLTING SHADOWS</div>
  <div class="tag heading">Interactive Horror Experience</div>
  <div class="info">The Ember Playhouse | June 1st, 2019<br>www.boltingshadows.com.au</div>
</section>

<section class="gallery abs">
  <div class="photo" role="img" aria-label="Event photo: costumed performer"></div>
  <div class="photo green" role="img" aria-label="Event photo: dark green lit room"></div>
  <div class="photo" role="img" aria-label="Event photo: pale horror character"></div>
  <div class="photo" role="img" aria-label="Event photo: group of guests"></div>
  <div class="photo" role="img" aria-label="Event photo: blood-stained performer"></div>
  <div class="photo" role="img" aria-label="Event photo: cast in blue light"></div>
  <div class="photo" role="img" aria-label="Event photo: checkered floor room"></div>
  <div class="photo" role="img" aria-label="Event photo: performer in red light"></div>
  <div class="photo" role="img" aria-label="Event photo: cast lineup"></div>
</section>

<div class="sec-title abs heading" style="top:1220px">
  <span class="kicker">Lorem</span>
  <h2>Lorem Ipsum</h2>
</div>
<section class="features abs">
  <div class="feature"><div class="box">LOREM IPSUM</div><span class="btn">Book Now</span></div>
  <div class="feature"><div class="box">LOREM IPSUM</div><span class="btn">Book Now</span></div>
  <div class="feature"><div class="box">LOREM IPSUM</div><span class="btn">Book Now</span></div>
  <div class="feature"><div class="box">LOREM IPSUM</div><span class="btn">Book Now</span></div>
</section>
<div class="dots abs"><i></i><i></i><i></i></div>

<section class="produced abs">
  <div class="photo-band" role="img" aria-label="Performers on a checkered floor"></div>
  <div class="green-band"></div>
  <div class="label heading">Produced<br>By</div>
  <div class="partner">MARBLE LANTERN<br>PRODUCTIONS</div>
</section>

<div class="sec-title abs heading" style="top:1850px">
  <span class="kicker">Next</span>
  <h2>Steps</h2>
</div>
<section class="steps abs heading">
  <div class="step">Purchase your <span>ticket here</span> for one of our waves</div>
  <div class="step">Rock up at the <span>Ember Playhouse</span> on June 1st at your wave time</div>
  <div class="step">Experience each of our <span>6 interactive</span> horror rooms</div>
  <div class="step">Grab some drinks at <span>the bar</span>, a bite to eat, and enjoy a <span>fantastic night out!</span></div>
</section>

<div class="sec-title plain abs heading" style="top:2150px" id="testimonials"><h2>Testimonials</h2></div>
<section class="testimonials abs">
  <div class="quote featured"><div class="card">Lorem ipsum is simply dummy text of the printing and typesetting industry. It has been the standard dummy text ever since.</div><div class="who"><span class="avatar"></span>LOREM IPSUM</div></div>
  <div class="quote"><div class="card">Lorem ipsum is simply dummy text of the printing and typesetting industry. It has been the standard dummy text.</div><div class="who"><span class="avatar"></span>LOREM IPSUM</div></div>
  <div class="quote"><div class="card">Lorem ipsum is simply dummy text of the printing and typesetting industry. It has been the standard dummy text.</div><div class="who"><span class="avatar"></span>LOREM IPSUM</div></div>
</section>

<div class="sec-title abs heading" style="top:2470px" id="faq"><h2 style="color:var(--green)">FAQs</h2></div>
<section class="faq abs">
  <div class="faq-item">Lorem Ipsum is simply dummy text of the printing and typesetting industry? <b>+</b></div>
  <div class="faq-item">Lorem Ipsum is simply dummy text of the printing and typesetting industry? <b>+</b></div>
  <div class="faq-item">Lorem Ipsum is simply dummy text of the printing and typesetting industry? <b>+</b></div>
  <div class="faq-item">Lorem Ipsum is simply dummy text of the printing and typesetting industry? <b>+</b></div>
  <div class="faq-item">Lorem Ipsum is simply dummy text of the printing and typesetting industry? <b>+</b></div>
  <div class="faq-item open">Lorem Ipsum is simply dummy text of the printing and typesetting industry? <b>–</b></div>
  <div class="faq-answer">Lorem Ipsum is simply dummy text of the printing and typesetting industry. Lorem Ipsum has been the industry's standard dummy text ever since the 1500s, when an unknown printer took a galley of type and scrambled it to make a type specimen book. It has survived not only five centuries, but also the leap into electronic typesetting, remaining essentially unchanged.</div>
</section>

<div class="sec-title book-title abs heading" style="top:2970px" id="contact"><h2>Book an Event</h2></div>
<p class="call abs">call us at (000) 000-0000 or fill out the form below and one of our staff members will reach out to confirm your event booking.</p>
<form class="form abs">
  <div class="field">Name</div>
  <div class="field">Email</div>
  <div class="field">Phone</div>
  <div class="field">Event Date</div>
  <div class="field">Group Size</div>
  <div class="field">Wave Time</div>
  <div class="field wide">Message</div>
</form>
<span class="btn submit abs">Submit Enquiry</span>

<div class="footer-brand abs">BOLTING SHADOWS</div>
<p class="copy abs">© 2019 Bolting Shadows. All Rights Reserved.</p>

</body>
</html>
```